Etiketten für Olivenöl-Intensivcreme
Zielgruppe
Wir produzieren Bio-Food, u.a. Wein und Olivenöl. Jetzt soll eine Olivenöl-Intensivcreme im Bereich Kosmetik auf dem Markt platziert werden. Unsere Zielgruppe hat ein sehr breites Altersspektrum (jung bis alt), ist naturverbunden, tierlieb, gebildet, kritisch-reflektierend, weiß gute Qualität zu schätzen, ist überwiegend weiblich. Die Olivenöl-Intensivcreme hat eine sehr breite Verwendung und soll sich als 'Allzweckwaffe' in jedem Haushalt etablieren (Babyhaut-Pflege, Lippenpflege, Ganzkörperpflege, Hand-Schutzcreme etc.).
Aufgabenstellung
Die Creme soll heißen: Tavunel (es könnte z.B. der Buchstabe 'O' durch eine Olive ersetzt werden). Es gibt zwei Etikette (Deckeloberseite der Metalldose und auf dem Boden). Der Durchmesser der Etikette ist jeweils 5,5 cm. Die Deckelunterseite gilt reinen Pflichtangaben. Im Dateidownloadbereich sind die Textvorgaben für die Etikette. MUT zur Farbe! Wir sind NICHT brav und angepasst! Orange kann Akzente setzen bzw. für Aufmerksamkeit im Regal sorgen.

```html
<!DOCTYPE html>
<html lang="de">
<head>
<meta charset="utf-8">
<title>Tavunel – Olivenöl-Intensivcreme Etikett</title>
<link rel="stylesheet" href="https://fonts.googleapis.com/css2?family=Roboto:wght@400;500;700&display=swap">
<style>
  :root {
    --page-bg: #eceae8;
    --label-top: #f4efb4;
    --label-bottom: #fdfcf3;
    --olive-green: #3f7a1c;
    --olive-dark: #2f5e14;
    --text-grey: #5b6459;
    --gold: #c9a646;
    --gold-light: #e6cf86;
  }
  html, body {
    margin: 0;
    padding: 0;
    width: 1200px;
    height: 1200px;
    overflow: hidden;
    background: var(--page-bg);
  }
  .canvas {
    position: relative;
    width: 1200px;
    height: 1200px;
  }
  .label-art {
    position: absolute;
    inset: 0;
  }
  .label-text {
    position: absolute;
    left: 0;
    width: 1200px;
    text-align: center;
    font-family: "Roboto", sans-serif;
    margin: 0;
  }
  .product-name {
    top: 230px;
    font-size: 120px;
    font-weight: 700;
    color: var(--olive-green);
    letter-spacing: 1px;
    line-height: 1;
  }
  .product-type {
    top: 366px;
    font-size: 40px;
    font-weight: 500;
    color: var(--text-grey);
    line-height: 1;
  }
  .claims {
    top: 438px;
    font-size: 36px;
    font-weight: 500;
    color: var(--text-grey);
    line-height: 43px;
  }
  .brand-mark {
    top: 940px;
    font-size: 36px;
    font-weight: 400;
    color: var(--gold);
    letter-spacing: 2px;
    line-height: 1;
  }
</style>
</head>
<body>
<div class="canvas">
  <svg class="label-art" width="1200" height="1200" viewBox="0 0 1200 1200">
    <defs>
      <linearGradient id="label-fill" x1="0" y1="0" x2="0" y2="1">
        <stop offset="0" stop-color="var(--label-top)"/>
        <stop offset="1" stop-color="var(--label-bottom)"/>
      </linearGradient>
      <linearGradient id="branch-fill" x1="0" y1="0" x2="0" y2="1">
        <stop offset="0" stop-color="#4d8a24"/>
        <stop offset="1" stop-color="var(--olive-dark)"/>
      </linearGradient>
      <linearGradient id="horse-fill" x1="0" y1="0" x2="0" y2="1">
        <stop offset="0" stop-color="var(--gold-light)"/>
        <stop offset="1" stop-color="#f6ecc6"/>
      </linearGradient>
      <clipPath id="label-clip">
        <circle cx="600" cy="600" r="448"/>
      </clipPath>
    </defs>
    <circle class="label-face" cx="600" cy="600" r="448" fill="url(#label-fill)"/>
    <g clip-path="url(#label-clip)">
      <path class="branch-left" role="img" aria-label="Olivenzweig mit Oliven und Blättern, links"
            d="M150 570 C260 590 360 650 450 720 C500 760 540 790 560 800 C500 860 440 930 380 1000 L150 1000 Z"
            fill="url(#branch-fill)" opacity="0.85"/>
      <path class="branch-right" role="img" aria-label="Olivenzweig mit Oliven und Blättern, rechts"
            d="M1050 570 C960 610 880 660 790 720 C750 745 720 760 705 770 C760 830 820 900 860 970 L1050 970 Z"
            fill="url(#branch-fill)" opacity="0.85"/>
    </g>
    <rect class="horse-illustration" role="img" aria-label="Goldene Illustration eines galoppierenden Pferdes"
          x="565" y="712" width="160" height="208" rx="30" fill="url(#horse-fill)"/>
  </svg>

  <p class="label-text product-name">Tavunel</p>
  <p class="label-text product-type">Olivenöl-Intensivcreme</p>
  <p class="label-text claims">Naturkosmetik<br>Bio-Olive<br>vegan<br>Pflege- und Schutzcreme</p>
  <p class="label-text brand-mark">KORVANI.HOF</p>
</div>
</body>
</html>
```